Web Re-Design for African Art Gallery

Introduction
We are an art gallery carrying artworks by contemporary African artists. We require a new, more modern website for our gallery.
The website idea. The key words we’d like to use to describe our website are - elegant, simple, uncluttered, easy to navigate, classy, interesting.
We’d like a website that is as uncluttered as possible; a simple, elegant website that lets viewers carry out the business of viewing our artworks online as easily as possible. A web site that is adventurous and arty without being complicated.
Our logo is a monochrome dark grey colour but this should not affect the colour scheme of the website. We are also open to a new logo if it is decidedly better than what we have at present, and would be willing to pay additionally for it if we take it.
Our audience is international. Art collectors worldwide looking for contemporary art. We do not want any African themed design.
Sections
The home page will have various sections – Artists, New Works, Publication, Mailing list, Exhibitions
Below are a list of gallery websites we like.
http://www.tarvelqonsik.example/
http://www.pembrowgallery.example/
http://www.dalefrunkwater.example/
http://www.quillopraxa.example/exhibitions/2011-12-13_velvet-arcades/
http://www.zot.vrbn.example/index.html
Requirement
We'd like a a home page template as well as a template for the sections in HTML.
We do not have a regular coder so we'd be happy to have the winning designer carry on with fitting the rest of the site to the template if the price is right.
Our present website is www.moonfernstudio.example. feel free to get logo, artwork pictures and any other material you might need from there.
Thanks

```html
<!DOCTYPE html>
<html lang="en">
<head>
<meta charset="utf-8">
<title>Moonfern Studio</title>
<link rel="stylesheet" href="https://fonts.googleapis.com/css2?family=Open+Sans:wght@400;600;700&display=swap">
<style>
:root{
  --orange:#e8701a;
  --amber:#f9a800;
  --ink:#1c1c1c;
  --text:#333;
  --muted:#8a8a8a;
  --rule:#d9d9d9;
  --panel:#e8e8e8;
  --footer:#ededed;
  --white:#fff;
}
*{box-sizing:border-box;margin:0;padding:0}
html,body{width:848px;height:1200px;overflow:hidden}
body{position:relative;background:var(--white);font-family:"Open Sans",Arial,sans-serif;color:var(--text)}
.abs{position:absolute}
.top-nav{left:0;top:0;width:848px;height:47px;background:linear-gradient(#fff,#f3f3f3);border-bottom:1px dashed #cfcfcf}
.top-nav a{position:absolute;top:16px;font-size:13px;color:var(--orange);text-decoration:none;transform:translateX(-50%);white-space:nowrap}
.top-nav .is-active{left:28px;top:0;width:73px;height:46px;background:#c4c4c4;transform:none;color:var(--ink);text-align:center;line-height:48px}
.brand{left:17px;top:73px;width:184px;height:75px;border:2px solid #555;box-shadow:3px 3px 4px rgba(0,0,0,.35);display:flex;align-items:center;justify-content:center;font-size:20px;font-weight:700;color:#3a3a3a}
.share{left:640px;top:86px;font-size:13.5px;color:var(--ink);white-space:nowrap}
.share-icon{top:85px;width:17px;height:17px;background:#666;border-radius:2px}
.search{left:637px;top:124px;width:152px;height:20px;border:1px solid #ccc;border-radius:10px;box-shadow:inset 1px 1px 2px rgba(0,0,0,.15);font-size:9px;color:#666;padding:3px 11px}
.search-go{left:784px;top:122px;width:23px;height:23px;border-radius:50%;background:#111;color:#fff;font-size:9px;text-align:center;line-height:22px}
.hero{left:17px;top:172px;width:813px;height:265px;border-radius:8px;overflow:hidden;
  background:
    radial-gradient(ellipse 230px 120px at 400px 300px,#e8521a 0,#f07a1c 35%,rgba(244,160,48,.9) 60%,rgba(251,211,122,0) 100%),
    radial-gradient(ellipse 160px 90px at 70px 40px,rgba(244,170,40,.8) 0,rgba(251,211,122,0) 100%),
    linear-gradient(90deg,#fdf6e0 0,#fdf1d2 60%,#fbe7a8 100%);
  box-shadow:0 3px 6px rgba(0,0,0,.2)}
.hero-arrow{top:252px;width:25px;height:95px;background:rgba(255,255,255,.75)}
.section-bar{left:22px;width:552px;height:26px;background:linear-gradient(90deg,var(--amber) 0,var(--amber) 80%,rgba(249,168,0,0) 100%);border-top:1px dashed #ddd;color:var(--white);font-size:16px;line-height:24px;padding-left:10px}
.section-bar .hand{position:absolute;top:3px;width:20px;height:19px}
.artist-box{left:24px;top:493px;width:553px;height:214px;border:1px solid #e3e3e3}
.artist{font-size:10px;color:var(--ink);white-space:nowrap}
.artist::before{content:"›";position:absolute;left:-12px;top:-2px;font-size:11px;font-weight:700}
.thumb{border:1px solid #bbb}
.frame{border:5px solid #1a1a1a}
.pager{top:884px;width:19px;height:19px;border-radius:50%;background:var(--amber);border:1px solid #d98f00}
.side-title{left:602px;font-size:17px;color:var(--ink)}
.news-head{left:604px;font-size:10.5px;color:var(--ink)}
.news-body{left:604px;width:230px;font-size:8.5px;line-height:13.5px;color:var(--muted);white-space:nowrap}
.news-date{left:603px;width:140px;height:20px;background:var(--panel);font-size:11px;color:var(--ink);padding:2px 0 0 6px}
.rule{left:605px;width:223px;height:1px;background:var(--rule)}
.more{right:25px;font-size:11px;color:var(--ink)}
.footer{left:0;top:1087px;width:848px;height:113px;background:var(--footer)}
.footer-text{font-size:9px;color:var(--ink);white-space:nowrap}
</style>
</head>
<body>

<nav class="abs top-nav">
  <a class="is-active">HOME</a>
  <a style="left:157px">ARTICLES</a>
  <a style="left:257px">PROFILES</a>
  <a style="left:357px">CONTACT</a>
  <a style="left:461px">LIVE CHAT</a>
  <a style="left:562px">GALLERY</a>
  <a style="left:670px">EXHIBITIONS</a>
  <a style="left:778px">MF-MAIL</a>
</nav>

<div class="abs brand">Moonfern Studio</div>

<div class="abs share">Shared With</div>
<span class="abs share-icon" style="left:721px"></span>
<span class="abs share-icon" style="left:742px"></span>
<span class="abs share-icon" style="left:764px"></span>
<span class="abs share-icon" style="left:786px"></span>

<div class="abs search">type your word here</div>
<div class="abs search-go">go</div>

<div class="abs hero" role="img" aria-label="Large illustration of an orange sketched flower on a pale cream background"></div>
<div class="abs hero-arrow" style="left:19px">
  <svg width="25" height="95" viewBox="0 0 25 95"><polyline points="16,20 4,48 16,76" fill="none" stroke="#222" stroke-width="1.2"/></svg>
</div>
<div class="abs hero-arrow" style="left:803px">
  <svg width="25" height="95" viewBox="0 0 25 95"><polyline points="9,20 21,48 9,76" fill="none" stroke="#222" stroke-width="1.2"/></svg>
</div>

<svg width="0" height="0" style="position:absolute">
  <defs>
    <g id="hand-icon" fill="#fff">
      <ellipse cx="9" cy="12" rx="6" ry="5"/>
      <rect x="3" y="2" width="3" height="9" rx="1.5" transform="rotate(-20 4.5 10)"/>
      <rect x="7" y="0.5" width="3" height="10" rx="1.5" transform="rotate(-5 8.5 10)"/>
      <rect x="11" y="1" width="3" height="10" rx="1.5" transform="rotate(12 12.5 10)"/>
      <rect x="14" y="4" width="3" height="8" rx="1.5" transform="rotate(30 15.5 10)"/>
      <rect x="1" y="10" width="3" height="6" rx="1.5" transform="rotate(-50 2.5 12)"/>
    </g>
  </defs>
</svg>

<div class="abs section-bar" style="top:462px;left:24px;padding-left:14px">Artists
  <svg class="hand" style="left:71px" viewBox="0 0 20 19"><use href="#hand-icon"/></svg>
</div>
<div class="abs artist-box"></div>

<div class="abs artist" style="left:56px;top:509px">Tobias Merrow</div>
<div class="abs artist" style="left:56px;top:530px">Anselm Vickery</div>
<div class="abs artist" style="left:56px;top:550px">Corin Halvey</div>
<div class="abs artist" style="left:56px;top:571px">Osric Pellam</div>
<div class="abs artist" style="left:56px;top:592px">Lucan Ferrier</div>
<div class="abs artist" style="left:56px;top:612px">Dorian Kestle</div>
<div class="abs artist" style="left:56px;top:633px">Mira Stovell</div>
<div class="abs artist" style="left:56px;top:654px">Elric Danwood</div>
<div class="abs artist" style="left:56px;top:674px">.Rolan Ashby</div>

<div class="abs artist" style="left:180px;top:509px">Silas Everitt</div>
<div class="abs artist" style="left:180px;top:530px">Teo Marchant</div>
<div class="abs artist" style="left:180px;top:550px">Aldo Kersey</div>
<div class="abs artist" style="left:180px;top:571px">Hollis Brayne</div>
<div class="abs artist" style="left:180px;top:592px">Ambrose Quill</div>
<div class="abs artist" style="left:180px;top:612px">Felix Jarrold</div>
<div class="abs artist" style="left:180px;top:633px">Bastian Oldcastle</div>
<div class="abs artist" style="left:180px;top:654px">Zane Orwell</div>
<div class="abs artist" style="left:180px;top:674px">Gideon Northam</div>

<div class="abs artist" style="left:314px;top:509px">Bram Osley</div>
<div class="abs artist" style="left:314px;top:530px">Kieran Ottley</div>
<div class="abs artist" style="left:314px;top:550px">Seth Ormsby</div>
<div class="abs artist" style="left:314px;top:571px">Marlow Oakden</div>
<div class="abs artist" style="left:314px;top:592px">Ivo Wexcombe</div>
<div class="abs artist" style="left:314px;top:612px">Boris Ashdale</div>
<div class="abs artist" style="left:314px;top:633px">Gareth Hulme</div>
<div class="abs artist" style="left:314px;top:654px">Elric Danwood</div>
<div class="abs artist" style="left:314px;top:674px">Milo Zarbeck</div>

<div class="abs artist" style="left:446px;top:509px">Tamsin Olliver</div>
<div class="abs artist" style="left:446px;top:530px">Basil Orrington</div>
<div class="abs artist" style="left:446px;top:550px">Jasper Burlow</div>
<div class="abs artist" style="left:446px;top:571px">Jonas Arkwell</div>
<div class="abs artist" style="left:446px;top:592px">Jerome Bexley</div>
<div class="abs artist" style="left:446px;top:612px">Nolan Ockley</div>
<div class="abs artist" style="left:446px;top:633px">Kit Argent</div>
<div class="abs artist" style="left:446px;top:654px">Emory Adlington</div>
<div class="abs artist" style="left:446px;top:674px">Yves Morrow</div>

<div class="abs section-bar" style="top:714px">Exhibitions
  <svg class="hand" style="left:100px" viewBox="0 0 20 19"><use href="#hand-icon"/></svg>
</div>
<div class="abs thumb" style="left:23px;top:757px;width:175px;height:109px;background:linear-gradient(135deg,#e9dcc0,#c9a878 50%,#8f9bb0)" role="img" aria-label="Abstract geometric painting with circles and lines"></div>
<div class="abs thumb" style="left:204px;top:757px;width:175px;height:109px;background:linear-gradient(135deg,#8b7fa8,#5f6e5a 50%,#9a9a9a)" role="img" aria-label="Collage of photographs of flowers, trees and buildings"></div>
<div class="abs thumb" style="left:386px;top:757px;width:175px;height:109px;background:linear-gradient(#eeeeec,#dcdad6 60%,#b68e64)" role="img" aria-label="White gallery room with framed artworks and wooden floor"></div>

<div class="abs section-bar" style="top:880px">Gallery
  <svg class="hand" style="left:71px" viewBox="0 0 20 19"><use href="#hand-icon"/></svg>
</div>
<svg class="abs pager" style="left:479px" viewBox="0 0 19 19"><polygon points="12,5 6,9.5 12,14" fill="#fff"/></svg>
<svg class="abs pager" style="left:506px" viewBox="0 0 19 19"><polygon points="7,5 13,9.5 7,14" fill="#fff"/></svg>

<div class="abs frame" style="left:22px;top:923px;width:176px;height:110px;background:linear-gradient(#f4f4f4,#e4e4ea)" role="img" aria-label="Purple flowers on tall stems against a white background"></div>
<div class="abs frame" style="left:204px;top:923px;width:176px;height:110px;background:linear-gradient(135deg,#9fd0ea,#3a6e92 55%,#1c2e3c)" role="img" aria-label="Silhouetted tree on a floating island under a blue sky"></div>
<div class="abs frame" style="left:386px;top:923px;width:176px;height:110px;background:linear-gradient(#1e3552,#35608c 55%,#d8a3b0)" role="img" aria-label="Fantasy castle on a snowy peak under stormy clouds"></div>

<div class="abs side-title" style="top:476px">Newsletter Mailing list</div>

<div class="abs news-head" style="top:517px">Heading goes here</div>
<p class="abs news-body" style="top:536px">The only way to success is through the right path and<br>that's what we provide you. None of the other compa-<br>nies has the result we do.</p>
<div class="abs news-date" style="top:579px">Posted on&nbsp; 25.Jan.2012</div>

<div class="abs news-head" style="top:618px">Heading goes here</div>
<p class="abs news-body" style="top:637px">The only way to success is through the right path and<br>that's what we provide you. None of the other compa-<br>nies has the result we do.</p>
<div class="abs news-date" style="top:681px">Posted on&nbsp; 25.Jan.2012</div>

<div class="abs news-head" style="top:726px">Heading goes here</div>
<p class="abs news-body" style="top:745px">The only way to success is through the right path and<br>that's what we provide you. None of the other compa-<br>nies has the result we do.</p>
<div class="abs news-date" style="top:789px">Posted on&nbsp; 25.Jan.2012</div>

<div class="abs rule" style="top:830px"></div>
<div class="abs more" style="top:830px">view more</div>

<div class="abs side-title" style="top:846px;font-size:15px">Publication</div>
<div class="abs thumb" style="left:603px;top:875px;width:110px;height:76px;background:linear-gradient(135deg,#e8a22a,#c64a1c 50%,#7aa0a8)" role="img" aria-label="Colourful expressionist painting in orange and red"></div>
<div class="abs thumb" style="left:721px;top:875px;width:110px;height:76px;background:linear-gradient(135deg,#4a6d8a,#7ea69a 50%,#c88a6a)" role="img" aria-label="Painted street scene in blue and green"></div>
<div class="abs thumb" style="left:603px;top:963px;width:110px;height:78px;background:linear-gradient(135deg,#3a2418,#8a5a3a 50%,#d8c0a0)" role="img" aria-label="Dark still life painting in browns"></div>
<div class="abs thumb" style="left:721px;top:963px;width:110px;height:78px;background:linear-gradient(135deg,#6a8ab0,#d8b890 50%,#8a9a7a)" role="img" aria-label="Painting of figures by a river in blue and ochre"></div>

<div class="abs rule" style="top:1055px"></div>
<div class="abs more" style="top:1055px">view more</div>

<footer class="abs footer"></footer>
<div class="abs footer-text" style="left:27px;top:1106px">Copyright © 2012 Company Name |&nbsp;&nbsp; All right reserved</div>
<div class="abs footer-text" style="left:27px;top:1125px">Privacy Policy &nbsp;|&nbsp; Terms &amp; Conditions</div>
<div class="abs footer-text" style="left:449px;top:1106px">Home | About Us | Contact Us | Live Chat | Gallery | Articles | Profiles | MF-Email</div>

</body>
</html>
```